Fact Sheets for Insurance

We need a 4 page booklet brochure designed for our insurance business. Each page is A4. We design insurance plans for our Clients and we wish to use the brochure to market and educate our Client and business partners. The business is Halvorsen Brightwick Financial Services. Colour scheme of our logo and stationary is navy blue and metallic gold. The content has been drafted and each page is attached. Please use your creative freedom to make it look professional and modern. We would like graphics, pictures etc to make it more vibrant as well.

Industry/Entity Type

Insurance

```html
<!DOCTYPE html>
<html lang="en">
<head>
<meta charset="utf-8">
<title>Halvorsen Brightwick – Insurance Cheat Sheets</title>
<link href="https://fonts.googleapis.com/css2?family=Libre+Baskerville:wght@400;700&family=Open+Sans:wght@400;600;700;800&display=swap" rel="stylesheet">
<style>
:root{
  --navy:#1d5177;
  --navy-deep:#123c61;
  --gold:#b9a36a;
  --gold-light:#d8c99a;
  --gold-text:#e8c95a;
  --grey-row:#c9ccd3;
  --panel:#e7eaf0;
  --paper:#f3f4f6;
  --ink:#1d2a3a;
  --link:#2f6f9e;
  --red:#b5282c;
  --white:#ffffff;
}
*{box-sizing:border-box;margin:0;padding:0}
html,body{width:1200px;height:422px;overflow:hidden;background:var(--white)}
body{font-family:"Open Sans",Arial,sans-serif;color:var(--ink)}
.canvas{position:relative;width:1200px;height:422px;display:flex;gap:2px}
.page{position:relative;width:298.5px;height:422px;overflow:hidden;background:var(--paper)}
.abs{position:absolute}
.photo{position:absolute;left:0;top:0;width:100%}

.tab-cheat{position:absolute;top:0;background:var(--gold);color:var(--white);font:700 11px "Open Sans",sans-serif;letter-spacing:.3px;padding:3px 10px 4px}
.brand{position:absolute;display:flex;align-items:center;gap:3px;font:700 6.5px "Open Sans",sans-serif;color:var(--white);line-height:1.1}
.brand .mark{width:7px;height:7px;background:var(--white);flex:none}
.brand.dark{color:var(--navy)}
.brand.dark .mark{background:var(--navy)}

.title-box{position:absolute;background:var(--navy);color:var(--white);font:700 11px/1.15 "Libre Baskerville",serif;text-transform:uppercase;padding:6px 8px;border-radius:0 0 8px 0}
.panel{position:absolute;background:var(--panel)}
.head{background:var(--navy);color:var(--white);font:800 7px "Open Sans",sans-serif;text-align:center;text-transform:uppercase;padding:4px 3px;line-height:1.1}
.head.gold{background:var(--gold)}

table.needs{width:100%;border-collapse:collapse;font-size:5.2px}
table.needs th{font-weight:800;text-align:left;padding:1.5px 8px;background:var(--panel)}
table.needs th.amt,table.needs td.amt{text-align:center}
table.needs td{padding:1.7px 8px;color:#fff}
table.needs tr.g td{background:var(--gold)}
table.needs tr.s td{background:var(--grey-row);color:#6a6f78}
table.needs tr.t td{background:var(--panel);color:var(--ink);font-weight:800}

.tips{padding:6px 7px;font-size:4.7px;line-height:1.45;font-weight:600}
.tips p{margin-bottom:6px}
.tips b{color:var(--link)}
.list{list-style:none;font-size:5.4px;font-weight:700;padding:6px 8px}
.list li{margin-bottom:3.5px;padding-left:8px;position:relative}
.list li::before{content:"";position:absolute;left:0;top:1px;border-left:3.5px solid var(--navy);border-top:2px solid transparent;border-bottom:2px solid transparent}
.help{font-size:5.2px;padding:6px 8px 0}
.list.small{font-size:4.6px;font-weight:600;padding-top:3px}
.promise{position:absolute;background:var(--navy);color:var(--white);font:400 7.6px/1.45 "Libre Baskerville",serif;font-variant:small-caps;text-align:center;padding:8px 9px;letter-spacing:.2px}
.promise .gold{display:block;margin-top:7px;color:var(--gold-text)}

.footer{position:absolute;left:0;bottom:0;width:100%;height:30px;background:var(--navy-deep);color:#cfd6e0;font-size:3.6px;line-height:1.4}
.pnum{position:absolute;font:400 20px "Open Sans",sans-serif}
.disclaimer{position:absolute;font-size:3.4px;line-height:1.35;color:#5f6670;text-align:center}
</style>
</head>
<body>
<main class="canvas">

<!-- PAGE 1 : TPD -->
<section class="page">
  <div class="photo" role="img" aria-label="Photo of an older man at home being cared for" style="height:240px;background:linear-gradient(160deg,#e9e3da 0%,#cbbfae 45%,#8c7d6c 100%)"></div>
  <div class="tab-cheat" style="left:0">CHEAT SHEET</div>
  <div class="brand" style="left:52px;top:22px;width:70px;flex-direction:column;align-items:flex-start"><span class="mark" style="width:14px;height:14px"></span><span>Halvorsen Brightwick</span></div>
  <div class="title-box" style="left:122px;top:12px;width:174px;font-size:9.5px;line-height:1.2;text-align:center;padding:6px 5px">Buying Total and<br>Permanent Disability<br>(TPD) Insurance</div>

  <div class="panel" style="left:15px;top:124px;width:136px;height:262px">
    <div class="head">How much do I need?</div>
    <table class="needs" style="margin-top:6px">
      <tr><th>NEED</th><th class="amt">AMOUNT</th></tr>
      <tr class="g"><td>Repaying Debts</td><td class="amt">$</td></tr>
      <tr class="s"><td>Medical Expenses</td><td class="amt">$</td></tr>
      <tr class="g"><td>Home Modification Costs</td><td class="amt">$</td></tr>
      <tr class="s"><td>Other</td><td class="amt">$</td></tr>
      <tr class="t"><td>TOTAL</td><td class="amt">$</td></tr>
    </table>
    <div class="head" style="margin-top:6px">Tips &amp; Traps</div>
    <div class="tips">
      <p><b>Purchase an "Own Occupation" definition Policy</b> to ensure that you are not tested against your ability to work in "Any Occupation" at claim time.</p>
      <p><b>Review what the policy doesn't cover "Exclusions".</b> Standard exclusion for most policies is self-inflicted acts.</p>
      <p>Look to <b>purchase "Long Term" Life Insurance</b> if you think you will need to hold the policy for a number of years. This may save you tens of thousands of dollars over the life of your policy.</p>
      <p>Ensure the contract is <b>guaranteed to be renewed</b> if you pay your premiums until expiry age.</p>
      <p>If purchased through Super, <b>you may be liable for a tax bill</b> in the event of a claim</p>
    </div>
  </div>

  <div class="panel" style="left:158px;top:128px;width:133px;height:84px">
    <div class="head">Who offers it?</div>
    <ul class="list">
      <li>Most Superannuation Funds</li><li>Some Private Health Funds</li><li>Some Employers</li><li>Life Insurance Companies</li><li>General Insurance Companies</li>
    </ul>
  </div>
  <div class="panel" style="left:158px;top:218px;width:133px;height:92px">
    <div class="head gold">When to call a professional adviser?</div>
    <p class="help">If you need help:</p>
    <ul class="list small">
      <li>comparing premiums or policies</li><li>reviewing wording of insurance contracts</li><li>matching a policy to suit your occupation purchasing "Long Term" Life Insurance</li><li>purchasing "Long Term" Life Insurance</li>
    </ul>
  </div>
  <div class="promise" style="left:158px;top:316px;width:133px;height:70px">If you want to ensure that you have someone assisting your family if a claim is ever needed to be made.</div>

  <footer class="footer">
    <span class="pnum" style="left:8px;top:1px;color:#fff">1</span>
    <div class="abs" style="left:30px;top:5px;color:var(--gold-light)">Authorised Partner<br>Member Network<br>Licensed Adviser</div>
    <div class="brand" style="left:108px;top:11px"><span class="mark"></span><span>Halvorsen Brightwick</span></div>
    <div class="abs" style="left:195px;top:6px">Suite 4, 12 Harbour Lane, Cronvale<br>T 02 5550 1234 &nbsp; E info@halvorsenbrightwick.example<br>Authorised Representative of Example Advice Pty Ltd</div>
  </footer>
</section>

<!-- PAGE 2 : CRITICAL ILLNESS -->
<section class="page">
  <div class="photo" role="img" aria-label="Soft-focus photo of a hospital corridor" style="height:422px;background:linear-gradient(180deg,#f1f3f6 0%,#dfe6ee 40%,#c6d2de 75%,#b4c2cf 100%)"></div>
  <div class="title-box" style="left:0;top:30px;width:278px;height:42px;font-size:10.3px;font-weight:400;white-space:nowrap;padding:15px 12px 0 16px;border-radius:0 0 10px 0;background:#2a6290">Buying Critical Illness Insurance</div>

  <div class="panel" style="left:18px;top:92px;width:127px;height:248px">
    <div class="head">How much do I need?</div>
    <table class="needs" style="margin-top:10px">
      <tr><th>NEED</th><th class="amt">AMOUNT</th></tr>
      <tr class="g"><td>Medical Expenses</td><td class="amt">$</td></tr>
      <tr class="s"><td>Other</td><td class="amt">$</td></tr>
      <tr class="t"><td>TOTAL</td><td class="amt">$</td></tr>
    </table>
    <div class="head" style="margin-top:18px">Tips &amp; Traps</div>
    <div class="tips">
      <p><b>Pay particular attention to the definitions for Cancer and Cardiovascular conditions</b> such as Heart Attack so you are aware of when you can claim.</p>
      <p><b>Review what the policy doesn't cover "Exclusions".</b> Standard exclusion for most policies is self-inflicted acts.</p>
      <p>Look to <b>purchase "Long Term" Life Insurance</b> if you think you will need to hold the policy for a number of years. This may save you tens of thousands of dollars over the life of your policy.</p>
      <p>Ensure the contract is <b>guaranteed to be renewed</b> if you pay your premiums until expiry age.</p>
    </div>
  </div>

  <div class="panel" style="left:158px;top:125px;width:127px;height:80px">
    <div class="head">Who offers it?</div>
    <ul class="list">
      <li>Some Private Health Funds</li><li>Some Employers</li><li>Life Insurance Companies</li><li>General Insurance Companies</li>
    </ul>
  </div>
  <div class="panel" style="left:158px;top:210px;width:127px;height:96px;background:var(--white)">
    <div class="head" style="font-size:7.6px">When to call a professional adviser?</div>
    <p class="help">If you need help:</p>
    <ul class="list small">
      <li>comparing premiums or policies</li><li>reviewing &amp; comparing policy terms and conditions</li><li>purchasing "Long Term" Life Insurance</li>
    </ul>
  </div>
  <div class="promise" style="left:158px;top:308px;width:127px;height:64px">If you want to ensure that you have someone assisting you if a claim is ever needed to be made.</div>

  <div class="brand dark" style="left:122px;top:390px;flex-direction:column;gap:2px"><span class="mark" style="width:12px;height:12px"></span><span>Halvorsen Brightwick</span></div>
  <span class="pnum" style="left:244px;top:392px;color:var(--red)">2</span>
</section>

<!-- PAGE 3 : LIFE -->
<section class="page">
  <div class="photo" role="img" aria-label="Photo of a smiling family together at a table" style="height:110px;background:linear-gradient(180deg,#d8b894 0%,#e6d3bd 55%,#f0e8df 100%)"></div>
  <div class="abs" style="left:0;top:54px;width:100%;text-align:center;font:700 10.5px 'Libre Baskerville',serif;color:#2f6f9e">BUYING LIFE INSURANCE</div>

  <div class="panel" style="left:15px;top:106px;width:131px;height:266px">
    <div class="head">How much do I need?</div>
    <table class="needs" style="margin-top:4px">
      <tr><th>NEED</th><th class="amt">AMOUNT</th></tr>
      <tr class="g"><td>Repaying Debts</td><td class="amt">$</td></tr>
      <tr class="s"><td>Funeral Expenses</td><td class="amt">$</td></tr>
      <tr class="g"><td>Replacing your Income</td><td class="amt">$</td></tr>
      <tr class="s"><td>Other</td><td class="amt">$</td></tr>
      <tr class="t"><td>TOTAL</td><td class="amt">$</td></tr>
    </table>
    <div class="head" style="margin-top:6px">Tips &amp; Traps</div>
    <div class="tips">
      <p>Ensure contract <b>covers all causes of death</b>, not just accidents.</p>
      <p><b>Review exclusions.</b> The only standard industry exclusion is "suicide within first 13 months of policy inception or reinstatement".</p>
      <p>Look to <b>purchase "Long Term" Life Insurance</b> if you think you will need to hold the policy for a number of years. This may save you tens of thousands of dollars over the life of your policy.</p>
      <p>Ensure the contract is <b>guaranteed to be renewed</b> if you pay your premiums until expiry age.</p>
      <p>If purchased through Super, <b>beneficiaries may be liable for a tax bill</b> in the event of a claim</p>
    </div>
  </div>

  <div class="panel" style="left:155px;top:128px;width:131px;height:80px">
    <div class="head">Who offers it?</div>
    <ul class="list">
      <li>Most Superannuation Funds</li><li>Some Private Health Funds</li><li>Some Employers</li><li>Life Insurance Companies</li><li>General Insurance Companies</li>
    </ul>
  </div>
  <div class="panel" style="left:155px;top:213px;width:131px;height:94px;background:var(--white)">
    <div class="head">When to call a professional adviser?</div>
    <p class="help">If you need help:</p>
    <ul class="list small">
      <li>comparing premiums or policies</li><li>reviewing wording of insurance contracts</li><li>structuring your policies to get a tax deduction</li><li>avoiding tax on any claim proceeds</li><li>purchasing "Long Term" Life Insurance</li>
    </ul>
  </div>
  <div class="promise" style="left:155px;top:312px;width:131px;height:60px">If you want to ensure that you have someone assisting your family if a claim is ever needed to be made.</div>

  <span class="pnum" style="left:26px;top:392px;color:var(--red)">3</span>
  <div class="brand dark" style="left:116px;top:388px;flex-direction:column;gap:2px"><span class="mark" style="width:12px;height:12px"></span><span>Halvorsen Brightwick</span></div>
</section>

<!-- PAGE 4 : INCOME PROTECTION -->
<section class="page">
  <div class="photo" role="img" aria-label="Faint background photo of a workplace" style="height:392px;background:linear-gradient(180deg,#e8ebef 0%,#f1f2f4 100%)"></div>
  <div class="tab-cheat" style="right:0">CHEAT SHEET</div>
  <div class="brand dark" style="left:224px;top:22px;flex-direction:column;align-items:flex-start;gap:2px"><span class="mark" style="width:12px;height:12px"></span><span>Halvorsen Brightwick</span></div>
  <div class="title-box" style="left:10px;top:22px;width:150px;font-size:10px;padding:5px 7px;border-radius:0 8px 8px 0">Buying Income Protection Insurance</div>

  <div class="panel" style="left:18px;top:78px;width:132px;height:276px">
    <div class="head">How much do I need?</div>
    <p style="font:700 5.4px/1.5 'Libre Baskerville',serif;color:var(--navy);text-align:center;padding:8px 8px 10px">Most people insure 75% of their income, which is the maximum benefit that Insurance Companies generally cover.</p>
    <div class="head">Tips &amp; Traps</div>
    <div class="tips">
      <p>Ensure Policy <b>covers all illnesses and injuries</b>, not just accidents.</p>
      <p><b>Review what the policy doesn't cover "Exclusions".</b> Standard exclusions include self-inflicted acts, pregnancy related illnesses and war related claims.</p>
      <p><b>Understand the definitions of "Total and Partial Disability"</b> so you know when you can make a claim.</p>
      <p>Look to <b>purchase "Long Term" Life Insurance</b> if you think you will need to hold the policy for a number of years. This may save you tens of thousands of dollars over the life of your policy.</p>
      <p>Ensure the contract is <b>guaranteed to be renewed</b> if you pay your premiums until expiry age.</p>
      <p>Paying the premiums yourself, will generally generally enable you to <b>claim a tax deduction</b></p>
    </div>
  </div>

  <div class="panel" style="left:165px;top:78px;width:127px;height:74px">
    <div class="head">Who offers it?</div>
    <ul class="list" style="padding-top:5px">
      <li>Most Superannuation Funds</li><li>Some Private Health Funds</li><li>Some Employers</li><li>Life Insurance Companies</li><li>General Insurance Companies</li>
    </ul>
  </div>
  <div class="panel" style="left:165px;top:156px;width:127px;height:96px">
    <div class="head gold">When to call a professional adviser?</div>
    <p class="help">If you need help:</p>
    <ul class="list small">
      <li>comparing premiums</li><li>reviewing &amp; comparing policy terms and conditions</li><li>matching a policy to suit your occupation</li><li>deciding on the appropriate Waiting Periods and Benefit Periods</li><li>purchasing "Long Term" Life Insurance</li>
    </ul>
  </div>
  <div class="promise" style="left:165px;top:256px;width:127px;height:98px;font-size:6.8px;line-height:1.4;padding:8px 8px">If you want to ensure that you have someone assisting you if a claim is ever needed to be made.<span class="gold">If your financial affairs are complex due to being self-employed or a high income earner.</span></div>

  <p class="disclaimer" style="left:18px;top:362px;width:270px">The information provided on this fact sheet is general advice only and does not take into account your objectives, financial situation and needs. Before acting on any information in this fact sheet you should consider the appropriateness of the advice having regard to your own objectives, financial situation and needs.</p>

  <footer class="footer">
    <div class="brand" style="left:78px;top:11px"><span class="mark"></span><span>Halvorsen Brightwick</span></div>
    <div class="abs" style="left:152px;top:6px">Suite 4, 12 Harbour Lane, Cronvale<br>T 02 5550 1234 &nbsp; E info@halvorsenbrightwick.example<br>Authorised Representative of Example Advice Pty Ltd</div>
    <span class="pnum" style="right:10px;top:1px;color:#fff">4</span>
  </footer>
</section>

</main>
</body>
</html>
```